Hi dear
Our company name is Corbel Homecare.
Our specialty is Maintenance, installation And repairing of home. We are working at this field From last 10 years. We have very experience and skill team.
We are looking for half van wrap design. We have Velmar cargo deluxe 2016 year . We are looking for A unique and memorable design. We are looking to keep this design for ever and keep it as a brand.
We have ready logo design.
Please make sure we really looking for a unique design.
Our services as follows
Electrical
Carpentry
Plumbing
Plastering
Flooring
Painting & Decorating
Fencing
Gutter
Decking.

Hi dear designers
I asked for half van design, please don’t design full van.
I need to be design the back of the van and half of the van next to the back.
Thanks

Home owner

Sans Serif

• Phone number, email, website
07900123456
07700 900417
Info@corbel-Homecare.com
Www.corbel-homecare.com

```html
<!DOCTYPE html>
<html lang="en">
<head>
<meta charset="utf-8">
<title>Corbel Homecare – Van Wrap Side Panels</title>
<link rel="stylesheet" href="https://fonts.googleapis.com/css2?family=Poppins:wght@600;800&display=swap">
<style>
  :root {
    --navy: #1f3a8c;
    --navy-deep: #162c70;
    --red: #d4202c;
    --white: #ffffff;
    --ink: #1d2230;
    --base: #2a2d33;
    --page: #f2f3f5;
    --pale: #dde6f2;
  }
  html, body {
    margin: 0;
    padding: 0;
    width: 1200px;
    height: 1200px;
    overflow: hidden;
    background: var(--page);
    font-family: "Poppins", sans-serif;
  }
  .canvas {
    position: relative;
    width: 1200px;
    height: 1200px;
  }
  .wrap-panel {
    position: absolute;
    left: 50px;
    width: 1100px;
    height: 500px;
    border-radius: 18px;
    overflow: hidden;
    background: var(--white);
    box-shadow: 0 2px 10px rgba(0,0,0,0.08);
  }
  .wrap-panel--driver { top: 60px; }
  .wrap-panel--passenger { top: 640px; }
  .panel-art {
    position: absolute;
    inset: 0;
    width: 100%;
    height: 100%;
  }
  .brand-name {
    position: absolute;
    margin: 0;
    color: var(--navy);
    font-weight: 800;
    line-height: 0.95;
    letter-spacing: 1px;
  }
  .brand-name span { display: block; }
  .brand-name .first { font-size: 96px; }
  .brand-name .second { font-size: 44px; letter-spacing: 4px; }
  .services {
    position: absolute;
    margin: 0;
    padding: 0;
    list-style: none;
    display: flex;
    flex-wrap: wrap;
    justify-content: center;
    gap: 2px 12px;
    color: var(--navy);
    font-weight: 600;
    font-size: 15px;
    text-transform: uppercase;
    letter-spacing: 0.3px;
  }
  .services li::before {
    content: "•";
    color: var(--red);
    margin-right: 5px;
  }
  .contact {
    position: absolute;
    font-weight: 800;
  }
  .contact .phone { font-size: 34px; letter-spacing: 0.5px; display: block; }
  .contact .web { font-size: 15px; font-weight: 600; display: block; }
  .contact--light { color: var(--white); }
  .contact--dark { color: var(--navy); }

  /* driver side */
  .wrap-panel--driver .brand-name { left: 680px; top: 70px; }
  .wrap-panel--driver .services { left: 640px; top: 270px; width: 420px; }
  .wrap-panel--driver .contact { left: 60px; top: 250px; }

  /* passenger side */
  .wrap-panel--passenger .brand-name { left: 360px; top: 80px; }
  .wrap-panel--passenger .services { left: 330px; top: 280px; width: 420px; }
  .wrap-panel--passenger .contact { left: 60px; top: 280px; }
</style>
</head>
<body>
<main class="canvas">

  <section class="wrap-panel wrap-panel--driver" aria-label="Driver side wrap panel">
    <svg class="panel-art" viewBox="0 0 1100 500" aria-hidden="true">
      <path d="M0 0 H440 L330 500 H0 Z" fill="var(--navy)"/>
      <path d="M440 0 H470 L360 500 H330 Z" fill="var(--navy-deep)"/>
      <circle cx="500" cy="200" r="150" fill="var(--navy)"/>
      <rect x="0" y="400" width="1100" height="100" fill="var(--base)"/>
      <rect x="240" y="430" width="480" height="12" fill="var(--red)"/>
    </svg>
    <h2 class="brand-name"><span class="first">CORBEL</span><span class="second">HOMECARE</span></h2>
    <ul class="services">
      <li>Electrical</li><li>Carpentry</li><li>Plumbing</li><li>Plastering</li><li>Flooring</li>
      <li>Painting &amp; Decorating</li><li>Fencing</li><li>Gutter</li><li>Decking</li>
    </ul>
    <p class="contact contact--light"><span class="phone">07900 123456</span><span class="web">www.corbel-homecare.com</span></p>
  </section>

  <section class="wrap-panel wrap-panel--passenger" aria-label="Passenger side wrap panel">
    <svg class="panel-art" viewBox="0 0 1100 500" aria-hidden="true">
      <path d="M760 0 H1100 V400 H770 C800 260 780 120 760 0 Z" fill="var(--navy)"/>
      <path d="M740 0 C765 130 785 260 755 400 H735 C765 260 745 130 720 0 Z" fill="var(--pale)"/>
      <path d="M1100 220 V400 H980 Z" fill="var(--red)"/>
      <circle cx="920" cy="210" r="150" fill="var(--navy)" stroke="var(--white)" stroke-width="14"/>
      <rect x="0" y="400" width="1100" height="100" fill="var(--base)"/>
      <rect x="240" y="430" width="480" height="12" fill="var(--red)"/>
    </svg>
    <h2 class="brand-name"><span class="first">CORBEL</span><span class="second">HOMECARE</span></h2>
    <ul class="services">
      <li>Electrical</li><li>Carpentry</li><li>Plumbing</li><li>Plastering</li><li>Flooring</li>
      <li>Painting &amp; Decorating</li><li>Fencing</li><li>Gutter</li><li>Decking</li>
    </ul>
    <p class="contact contact--dark"><span class="phone">07900 123456</span><span class="web">www.corbel-homecare.com</span></p>
  </section>

</main>
</body>
</html>
```